Corridor Works

Small ageny public transit advocacy, funding and compliance.
Consulting and lobbying efforts for small public transit agencies and communities exploring public transit opportunities.

I was interested in a simple line sketch suggesting motion, mobility. The card will be black on white. I would like it to include the bUs ones brief; Advocacy, Funding , and Compliance for small transit agencies.

Reason: I have been traveling and have had limited time to respond. Thank you all for your submit talks.

Industry/Entity Type

Consulting

Contact Information for Business Card

Paul R Vesby
Phone (907) 418-2960
Email paulrvesby@mailnook.net

```html
<!DOCTYPE html>
<html lang="en">
<head>
<meta charset="utf-8">
<title>Paul R Vesby — Business Card</title>
<link rel="stylesheet" href="https://fonts.googleapis.com/css2?family=Noto+Sans:wght@400;600;700&display=swap">
<style>
  :root {
    --brand-blue: #27368f;
    --card-white: #ffffff;
    --stage-grey: #e8e8e9;
    --text-grey: #6b6b70;
    --ghost-tint: #f1f1f7;
  }
  * { box-sizing: border-box; margin: 0; padding: 0; }
  html, body {
    width: 1200px;
    height: 1000px;
    overflow: hidden;
  }
  body {
    background: var(--stage-grey);
    font-family: "Noto Sans", "Open Sans", Arial, sans-serif;
    position: relative;
  }
  .business-card {
    position: absolute;
    left: 93px;
    top: 213px;
    width: 1014px;
    height: 574px;
    background: var(--card-white);
    overflow: hidden;
  }
  .ghost-name {
    position: absolute;
    left: 112px;
    top: 222px;
    font-size: 112px;
    font-weight: 400;
    letter-spacing: 10px;
    color: var(--ghost-tint);
    white-space: nowrap;
    line-height: 1;
    user-select: none;
  }
  .name-tab {
    position: absolute;
    left: 0;
    top: 84px;
    width: 400px;
    height: 122px;
    background: var(--brand-blue);
    border-radius: 0 61px 61px 0;
    display: flex;
    align-items: center;
    padding-left: 60px;
  }
  .name-tab__name {
    color: var(--card-white);
    font-size: 41px;
    font-weight: 600;
    letter-spacing: 2.5px;
    white-space: nowrap;
  }
  .service-tagline {
    position: absolute;
    right: 76px;
    top: 112px;
    text-align: left;
    color: var(--brand-blue);
    font-size: 24px;
    font-weight: 700;
    letter-spacing: 1.4px;
    line-height: 42px;
    text-transform: uppercase;
  }
  .service-description {
    position: absolute;
    right: 85px;
    top: 339px;
    text-align: right;
    color: var(--text-grey);
    font-size: 22px;
    letter-spacing: 1px;
    line-height: 42px;
  }
  .contact-list {
    position: absolute;
    left: 60px;
    top: 423px;
    list-style: none;
    font-size: 25px;
    line-height: 42px;
    letter-spacing: 0.6px;
  }
  .contact-list__value { color: var(--brand-blue); }
  .contact-list__label { color: var(--text-grey); }
</style>
</head>
<body>
  <article class="business-card">
    <div class="ghost-name" aria-hidden="true">Paul R Vesby</div>

    <header class="name-tab">
      <h1 class="name-tab__name">Paul R Vesby</h1>
    </header>

    <p class="service-tagline">Public transit advocacy,<br>funding and compliance.</p>

    <p class="service-description">
      Consulting and lobbying efforts<br>
      for small public transit agencies<br>
      and communities exploring<br>
      public transit opportunities.
    </p>

    <ul class="contact-list">
      <li><span class="contact-list__value">(907) 418-2960</span> <span class="contact-list__label">(phone)</span></li>
      <li><span class="contact-list__value">paulrvesby@mailnook.net</span> <span class="contact-list__label">(e-mail)</span></li>
    </ul>
  </article>
</body>
</html>
```